Certificate of Completion - Educational Trainings

We are looking for a certificate of completion for individuals who complete one of our specific trainings. Files should be provided in a Word (docx) or PowerPoint (pptx) format. The "Halvorcrest example.png" file is to show necessary information. Copies of logos have been included for design purposes.

Target Market(s)

Training Participants

Industry/Entity Type

Healthcare

Font styles to use
Sans Serif

```html
<!DOCTYPE html>
<html lang="en">
<head>
<meta charset="UTF-8">
<title>Halvorcrest Certificate of Completion</title>
<link href="https://fonts.googleapis.com/css2?family=Montserrat:wght@400;500;600;700;800&display=swap" rel="stylesheet">
<style>
  :root {
    --page-bg: #e9eaea;
    --paper: #ffffff;
    --paper-edge: #dcdcdc;
    --green-dark: #12632b;
    --green-mid: #3fae2a;
    --green-bright: #7ed957;
    --ink: #111111;
  }
  * { margin: 0; padding: 0; box-sizing: border-box; }
  html, body {
    width: 800px; height: 1200px; overflow: hidden;
    background: var(--page-bg);
    font-family: 'Montserrat', sans-serif;
    color: var(--ink);
  }
  .certificate {
    position: absolute; left: 20px; top: 306px;
    width: 760px; height: 587px;
    background: radial-gradient(ellipse at 50% 55%, var(--paper) 35%, var(--paper-edge) 100%);
    box-shadow: 0 4px 14px rgba(0,0,0,0.25);
    overflow: hidden;
  }
  .corner-wave { position: absolute; }
  .corner-wave.top-right {
    right: 0; top: 0; width: 320px; height: 340px;
    background: radial-gradient(ellipse at 100% 0%, rgba(126,217,87,0.85) 0%, rgba(126,217,87,0.45) 40%, rgba(126,217,87,0) 72%);
  }
  .corner-wave.bottom-left {
    left: 0; bottom: 0; width: 170px; height: 300px;
    background: radial-gradient(ellipse at 0% 100%, rgba(126,217,87,0.85) 0%, rgba(126,217,87,0.45) 40%, rgba(126,217,87,0) 72%);
  }
  .line-text {
    position: absolute; left: 0; width: 760px; text-align: center; white-space: nowrap;
  }
  .brand {
    top: 46px; font-size: 21px; font-weight: 700; letter-spacing: 1.5px;
    display: flex; justify-content: center; align-items: center; gap: 8px;
  }
  .brand-dot { width: 16px; height: 16px; border-radius: 50%; background: var(--green-dark); }
  .address { top: 90px; font-size: 10.5px; line-height: 12.6px; }
  .title-main { top: 138px; font-size: 52px; font-weight: 800; color: var(--green-dark); letter-spacing: 0.5px; line-height: 1; }
  .title-sub { top: 196px; font-size: 27px; font-weight: 800; line-height: 1; }
  .awarded { top: 231px; font-size: 16px; letter-spacing: 3px; font-weight: 400; }
  .name-line { position: absolute; left: 201px; width: 362px; top: 307px; height: 1.5px; background: var(--green-dark); }
  .course-lead { top: 321px; font-size: 15px; font-weight: 700; }
  .course-name { top: 346px; font-size: 15px; font-weight: 500; color: var(--green-dark); }
  .course-details { top: 372px; font-size: 12.5px; line-height: 17.6px; font-weight: 500; }
  .seal-name {
    position: absolute; left: 325px; top: 478px; width: 116px; text-align: center;
    font-size: 13px; font-weight: 700; letter-spacing: 1px; color: var(--green-dark);
  }
  .signature { position: absolute; top: 482px; width: 124px; text-align: center; }
  .signature-line { height: 1.5px; background: var(--green-dark); margin-bottom: 7px; }
  .signature-label { font-size: 11.5px; font-weight: 700; white-space: nowrap; }
  .signature.date { left: 195px; }
  .signature.consultant { left: 438px; }
  .footnote { top: 527px; font-size: 8.2px; line-height: 10px; font-weight: 600; text-transform: uppercase; }
</style>
</head>
<body>
  <main class="certificate">
    <div class="corner-wave top-right" role="img" aria-label="Decorative green wave in the top right corner"></div>
    <div class="corner-wave bottom-left" role="img" aria-label="Decorative green wave in the bottom left corner"></div>

    <div class="line-text brand"><span class="brand-dot"></span>HALVORCREST</div>
    <p class="line-text address">48 harbor lane, ste. 12<br>brookfield, ME 04999<br>national registry sponsor number 70312</p>

    <h1 class="line-text title-main">CERTIFICATE</h1>
    <h2 class="line-text title-sub">OF COMPLETION</h2>
    <p class="line-text awarded">THIS CERTIFICATE IS AWARDED TO</p>

    <div class="name-line"></div>

    <p class="line-text course-lead">For successful completion of Best Practices</p>
    <p class="line-text course-name">Budget Process/Budget Building</p>
    <p class="line-text course-details">Completed Online<br>Field of Study Finance<br>CPE Credits : 1</p>

    <p class="seal-name">HALVORCREST</p>

    <div class="signature date"><div class="signature-line"></div><p class="signature-label">Completion date</p></div>
    <div class="signature consultant"><div class="signature-line"></div><p class="signature-label">Senior consultant</p></div>

    <p class="line-text footnote">In accordance with the standard of the National Council of Training Sponsors, CPE credits have<br>been granted based on a 50 minute hour.</p>
  </main>
</body>
</html>
```